Label design: italian artisan honey (to allow tradition look attractive!)

Founded in 1973, this specialized business in artisan honey, is based in Emilia-Romagna. It accounts for 10 apiary locations, honey is organic, whereas the equipment to rise, and control bees are all hand made.
The symbol, (you will find the logo corvasti.ai) is a hexagonal hunting house built in the 17th century. The structure is protected by fine-arts and retains its stucco works and frescoes depicting mythological scenes. The place is located in the hills, next to a hunting area, and surrounded by our ecological farm.

Please find the foto of the label that has been used for over 30 years and also the Italian Beekeeper association label that is placed on all the vases.

Target Market(s)

Local gastronomic shop owners, where local consumers are both young and mature families, well-read, connaisseurs, curious, with strong social ties also with nature.

Font styles to use
Serif
Sans Serif

Requirements
Must have
• We have a glass jar already with specific dimensions.
The lid finishing is metallic finishing, in copper color.
We need the label to have the by-law necessary information of the product on it:
Honey type, producer name, weight, best by date, origin.
The lid measures 6 cm in diameter, and has a border of about 0.5 cm.
The visible part of the glass jar is 3 cm high.
You can get inspired by the type of package we want to use: (in light wood or carton board as materials as in the 2 examples we attach is actually like a matchbox).
We also attached an illustrator file with the logo shape, colors to be adapted to your design, consider the "grey color" and the "metallic finishing" on the corner, as shown in the file ref_glimfold_3.
Nice to have
• The _pack_1 and _pack_3 files are mood ideas for the box, to provide you inspiration for the label.
The color palette is provided by two files :
ref_glimfold_3 ;
color_palette_corvasti.
The font reference is provided by two files :
Typeface ;
ref_typeface.

```html
<!DOCTYPE html>
<html lang="it">
<head>
<meta charset="utf-8">
<title>Corvasti – etichette miele</title>
<link href="https://fonts.googleapis.com/css2?family=Quicksand:wght@300;400;500;700&family=Baloo+2:wght@700;800&family=Open+Sans:wght@400&display=swap" rel="stylesheet">
<style>
  :root{
    --paper:#ffffff;
    --slate:#42514b;
    --gold:#c8900f;
    --copper:#a77a2e;
    --band-light:#e0d8c2;
    --band-dark:#c8bc9b;
    --ink:#4a5350;
    --ink-soft:#5e625c;
    --guide:#e3e3e3;
    --flag-green:#3d9a48;
    --flag-red:#cf4a26;
  }
  *{margin:0;padding:0;box-sizing:border-box}
  html,body{width:1200px;height:848px;overflow:hidden;background:var(--paper)}
  .sheet{position:relative;width:1200px;height:848px}
  .label{position:absolute;top:160px;width:525px;height:520px}
  .label--acacia{left:52px}
  .label--tiglio{left:633px}
  .label svg{position:absolute;left:0;top:0}
  .txt{position:absolute;font-family:"Quicksand",sans-serif;white-space:nowrap}
  .center{left:0;width:525px;text-align:center}
  .brand{top:214px;font-weight:400;font-size:0;color:#fff}
  .brand-name{top:158px;font-size:23px;font-weight:400;color:#fff;letter-spacing:.5px}
  .honey-type{top:200px;font-family:"Baloo 2",sans-serif;font-weight:800;font-size:21px;line-height:20px;color:var(--gold)}
  .stem-name{top:438px;font-size:10px;font-weight:400;color:#fff}
  .producer{left:12px;top:444px;font-size:9px;letter-spacing:2.4px;color:var(--ink-soft);font-weight:500}
  .web{left:4px;top:457px;font-family:"Open Sans",sans-serif;font-size:6.4px;color:var(--ink-soft)}
  .address{left:12px;top:471px;width:60px;text-align:center;font-family:"Open Sans",sans-serif;font-size:6px;line-height:9.8px;color:var(--ink-soft)}
  .origin{top:470px;font-family:"Baloo 2",sans-serif;font-weight:700;font-size:14px;line-height:13px;color:var(--slate)}
  .made-in{top:502px;left:0;width:525px;text-align:center;font-family:"Baloo 2",sans-serif;font-weight:700;font-size:8px;letter-spacing:.6px;color:#2f3a36}
  .best-by{right:8px;top:430px;text-align:right;font-family:"Open Sans",sans-serif;font-size:6.4px;line-height:8px;color:var(--ink-soft)}
  .lot{left:451px;top:467px;font-size:9.5px;line-height:9.5px;color:var(--ink);font-weight:500}
  .weight{right:8px;top:480px;font-size:32px;font-weight:400;color:var(--ink);letter-spacing:.5px}
</style>
</head>
<body>
<main class="sheet">

  <section class="label label--acacia" aria-label="Etichetta Miele di Acacia">
    <svg width="525" height="520" viewBox="0 0 525 520">
      <defs>
        <linearGradient id="band-a" x1="0" y1="0" x2="1" y2="1">
          <stop offset="0" stop-color="#ddd5be"/><stop offset=".5" stop-color="#d6cdb2"/><stop offset="1" stop-color="#c6b995"/>
        </linearGradient>
      </defs>
      <circle class="lid-guide" cx="263" cy="152" r="146" fill="none" stroke="#e3e3e3" stroke-width=".8"/>
      <rect class="band" x="0" y="424" width="525" height="96" fill="url(#band-a)" role="img" aria-label="Fondo con illustrazione di fiori di campo"/>
      <line x1="180" y1="479" x2="237" y2="479" stroke="#a77a2e" stroke-width="1"/>
      <line x1="289" y1="479" x2="346" y2="479" stroke="#a77a2e" stroke-width="1"/>
      <rect x="206" y="501" width="114" height="13" rx="6.5" fill="#fff" stroke="#a77a2e" stroke-width="1.2"/>
      <rect x="207" y="502" width="38" height="11" rx="5.5" fill="#3d9a48"/>
      <rect x="281" y="502" width="38" height="11" rx="5.5" fill="#cf4a26"/>
      <rect x="240" y="502" width="8" height="11" fill="#3d9a48"/>
      <rect x="278" y="502" width="8" height="11" fill="#cf4a26"/>
      <path class="tag" d="M229,261 A114,114 0 1 1 297,261 L297,445 L263,460 L229,445 Z" fill="#42514b" stroke="#a77a2e" stroke-width="2.5"/>
      <circle cx="263" cy="100" r="26" fill="#c8900f"/>
      <circle cx="263" cy="424" r="9" fill="#c8900f"/>
    </svg>
    <p class="txt center brand-name">CORVASTI</p>
    <p class="txt center honey-type" style="top:206px">MIELE DI<br>ACACIA</p>
    <p class="txt center stem-name">CORVASTI</p>
    <p class="txt producer">CORVASTI</p>
    <p class="txt web">www.mielecorvasti.com</p>
    <p class="txt address">Via Castellari, 22<br>Piacenza, Italy<br>Tel.0523.40.18.76<br>347.2085519</p>
    <p class="txt center origin">MIELE<br>PIACENTINO</p>
    <p class="txt made-in">PRODOTTO IN ITALIA</p>
    <p class="txt best-by">Consumare<br>preferibilmente entro:</p>
    <p class="txt lot">Lotto:<br>Peso:</p>
    <p class="txt weight">150g</p>
  </section>

  <section class="label label--tiglio" aria-label="Etichetta Miele di Tiglio">
    <svg width="525" height="520" viewBox="0 0 525 520">
      <defs>
        <linearGradient id="band-t" x1="0" y1="0" x2="1" y2="1">
          <stop offset="0" stop-color="#ddd5be"/><stop offset=".5" stop-color="#d6cdb2"/><stop offset="1" stop-color="#c6b995"/>
        </linearGradient>
      </defs>
      <circle class="lid-guide" cx="263" cy="152" r="146" fill="none" stroke="#e3e3e3" stroke-width=".8"/>
      <rect class="band" x="0" y="424" width="525" height="96" fill="url(#band-t)" role="img" aria-label="Fondo con illustrazione di fiori di campo"/>
      <line x1="180" y1="479" x2="237" y2="479" stroke="#a77a2e" stroke-width="1"/>
      <line x1="289" y1="479" x2="346" y2="479" stroke="#a77a2e" stroke-width="1"/>
      <rect x="206" y="501" width="114" height="13" rx="6.5" fill="#fff" stroke="#a77a2e" stroke-width="1.2"/>
      <rect x="207" y="502" width="38" height="11" rx="5.5" fill="#3d9a48"/>
      <rect x="281" y="502" width="38" height="11" rx="5.5" fill="#cf4a26"/>
      <rect x="240" y="502" width="8" height="11" fill="#3d9a48"/>
      <rect x="278" y="502" width="8" height="11" fill="#cf4a26"/>
      <path class="tag" d="M229,261 A114,114 0 1 1 297,261 L297,445 L263,460 L229,445 Z" fill="#42514b" stroke="#a77a2e" stroke-width="2.5"/>
      <circle cx="263" cy="100" r="26" fill="#c8900f"/>
      <circle cx="263" cy="424" r="9" fill="#c8900f"/>
    </svg>
    <p class="txt center brand-name">CORVASTI</p>
    <p class="txt center honey-type" style="top:206px">MIELE DI<br>TIGLIO</p>
    <p class="txt center stem-name">CORVASTI</p>
    <p class="txt producer">CORVASTI</p>
    <p class="txt web">www.mielecorvasti.com</p>
    <p class="txt address">Via Castellari, 22<br>Piacenza, Italy<br>Tel.0523.40.18.76<br>347.2085519</p>
    <p class="txt center origin">MIELE<br>PIACENTINO</p>
    <p class="txt made-in">PRODOTTO IN ITALIA</p>
    <p class="txt best-by">Consumare<br>preferibilmente entro:</p>
    <p class="txt lot">Lotto:<br>Peso:</p>
    <p class="txt weight">150g</p>
  </section>

</main>
</body>
</html>
```